Project management consultancy needs a website designed

Our company (Keystone PMO) currently has a website (http://www.keystonepmo-example.com.au) that needs to be re-designed and enhanced. Company is a professional services/consultancy business focused on project management. We are looking for something more professional. It would be advantageous if the website can be hosted in SharePoint. We are reasonably happy with the content, what we're after is something that has better aesthetics. Attached to the brief is a copy of our logo in vector format.

Target Market(s)

Small to medium businesses

Industry/Entity Type

It Company

Contact Information for Business Card

logo/company name on back, contact details plus smaller logo on front. Information to display = Name, title, address, phone number, email address, website address

Coding

Coded - Design and coding required

Number of Pages Required

4 page

Font styles to use
Sans Serif

Requirements
Must have
• Website must have: A home page, content page, contact details page (including a contact us function), blog. Project management related images/photos
Nice to have
• Website has the ability to support video content

```html
<!DOCTYPE html>
<html lang="en">
<head>
<meta charset="utf-8">
<title>Keystone Portfolio Management Office</title>
<link rel="stylesheet" href="https://fonts.googleapis.com/css2?family=Oswald:wght@400;500&family=Open+Sans:wght@300;400;600&family=Playfair+Display:wght@400&display=swap">
<style>
:root{
  --ink:#2b2b2b;
  --text:#555555;
  --dark:#1c1f22;
  --accent:#f0b24a;
  --accent-soft:#f5d9a6;
  --yellow:#e8d46a;
  --white:#ffffff;
  --field:#cfcfcf;
}
*{box-sizing:border-box;margin:0;padding:0}
html,body{width:1200px;height:3788px;overflow:hidden;background:var(--white)}
body{position:relative;font-family:"Open Sans",Arial,sans-serif;color:var(--text)}
.abs{position:absolute;left:0;width:1200px}

/* header */
.hero{top:0;height:492px;background:linear-gradient(180deg,#2a2f34 0%,#15181b 55%,#0f1113 100%)}
.main-nav{top:36px;display:flex;justify-content:center;font-size:13px;color:var(--white);letter-spacing:.5px}
.main-nav span{padding:0 14px;border-left:1px solid rgba(255,255,255,.5)}
.main-nav span:first-child{border-left:none}
.hero-title{top:160px;text-align:center;font-family:"Oswald",Arial,sans-serif;font-weight:500;font-size:46px;color:var(--white);letter-spacing:1px}
.hero-sub{top:232px;text-align:center;font-size:24px;color:var(--yellow);font-weight:400}
.brand{display:flex;align-items:center;justify-content:center;gap:20px}
.brand .mark{width:64px;height:64px;background:#2f82c9;border-radius:6px}
.brand .name{font-family:"Open Sans",Arial,sans-serif;font-weight:400;font-size:54px;color:var(--white);letter-spacing:1px}
.hero-brand{top:352px}

/* features */
.feature{position:absolute;top:608px;width:300px;text-align:center}
.feature .photo{width:224px;height:224px;border-radius:50%;margin:0 auto}
.feature h3{margin-top:68px;font-weight:300;font-size:40px;color:#333;letter-spacing:1px}
.divider-top{top:1056px;height:2px;background:var(--accent-soft)}

/* content */
.section-title{text-align:center;font-family:"Playfair Display",Georgia,serif;font-weight:400;font-size:36px;line-height:48px;color:var(--ink);letter-spacing:1px}
.rule{height:2px;width:300px;margin:0 auto;background:var(--accent)}
.copy{width:760px;left:220px;text-align:center;font-size:17px;line-height:28px}

/* contact */
.quick{top:2996px}
.quick-head{display:flex;align-items:center;justify-content:center;gap:18px;margin-top:22px}
.quick-head svg{display:block}
.quick-head span{font-size:40px;color:#333;font-weight:400}
.form{position:absolute;top:3116px;left:440px;width:330px;font-size:14px;color:#333}
.row{display:flex;align-items:flex-start;margin-bottom:12px}
.row label{width:80px}
.row .field{width:244px;height:24px;border:1px solid var(--field)}
.row .area{height:136px}

/* footer */
.footer{top:3472px;height:316px;background:linear-gradient(180deg,#23272b 0%,#121416 100%)}
.footer-brand{top:3510px}
.social{top:3608px;display:flex;justify-content:center;gap:8px}
.social span{width:64px;height:64px;border-radius:50%;background:#7a7d80}
.foot-nav{top:3716px;border-top:1px solid rgba(232,212,106,.6);padding-top:4px}
.foot-nav.main-nav{font-size:12px;color:var(--yellow)}
.foot-nav.main-nav span{border-left-color:rgba(232,212,106,.6)}
.copyright{top:3756px;text-align:center;font-size:12px;color:var(--white)}
</style>
</head>
<body>

<header>
  <div class="abs hero" role="img" aria-label="Dark photograph of modern office buildings at dusk"></div>
  <nav class="abs main-nav">
    <span>HOME</span><span>WHAT IS A PMO</span><span>HOW DOES A PMO ADD VALUE</span><span>WHAT'S THE ADVANTAGE</span><span>WHY KEYSTONE PMO</span><span>CONTACT US</span><span>BLOG</span>
  </nav>
  <h1 class="abs hero-title">KEYSTONE PORTFOLIO MANAGEMENT OFFICE</h1>
  <p class="abs hero-sub">Offering you a competitive alternative to traditional in-house PMOs</p>
  <div class="abs brand hero-brand"><span class="mark"></span><span class="name">KEYSTONE PMO</span></div>
</header>

<section>
  <div class="feature" style="left:114px">
    <div class="photo" role="img" aria-label="Photo of a business handshake over a green field" style="background:radial-gradient(circle at 50% 35%,#c9d3da 0%,#8a9a8c 55%,#4f7a3c 100%)"></div>
    <h3>OUR TEAM</h3>
  </div>
  <div class="feature" style="left:450px">
    <div class="photo" role="img" aria-label="Photo of a bright modern office interior" style="background:radial-gradient(circle at 50% 40%,#ffffff 0%,#e4e6e7 55%,#a9adb0 100%)"></div>
    <h3>WE AIM</h3>
  </div>
  <div class="feature" style="left:826px">
    <div class="photo" role="img" aria-label="Photo of a glass office tower against the sky" style="background:linear-gradient(160deg,#b9c9d8 0%,#7f8f9c 50%,#4a5560 100%)"></div>
    <h3>WE PROVIDE</h3>
  </div>
  <div class="abs divider-top"></div>
</section>

<main>
  <h2 class="abs section-title" style="top:1184px">OUR TEAM</h2>
  <div class="abs" style="top:1244px"><div class="rule"></div></div>
  <p class="abs copy" style="top:1316px">Our team of professionals comes equipped with a wealth of experience in both the private and public sectors. Let our professionally certified experts monitor and improve your project management so that you can focus on your business.</p>

  <div class="abs" style="top:1492px"><div class="rule"></div></div>
  <h2 class="abs section-title" style="top:1508px">WE AIM</h2>
  <p class="abs copy" style="top:1636px">We aim to align the selection and execution of projects and programs with your organization's business goals, thereby increasing the success of project execution. We provide coordination, guidance, and training to your project teams, coaching them in your company's methodologies and standards for each project.</p>

  <div class="abs" style="top:1864px"><div class="rule"></div></div>
  <h2 class="abs section-title" style="top:1876px">MOST IMPORTANTLY</h2>
  <p class="abs copy" style="top:2000px">Most importantly, we work with you to implement these strategies in a way that works with your individual organization and fits your specific needs.</p>

  <div class="abs" style="top:2152px"><div class="rule"></div></div>
  <h2 class="abs section-title" style="top:2164px">WE PROVIDE</h2>
  <p class="abs copy" style="top:2290px">We provide the tools, knowledge and experience so that you will have confidence in the overall management of your projects and get back to concentrating on your business. Keystone PMO will allow you to:</p>
  <p class="abs copy" style="top:2464px">Optimize the use of your capital. We'll help you avoid project inefficiency and maximize success by choosing the right projects the first time, every time.</p>
  <p class="abs copy" style="top:2584px">Filter out the noise; you have enough on your plate without being inundated with data. We'll communicate efficiently to provide you with the important information you need.</p>
  <p class="abs copy" style="top:2704px">Let Project Managers focus on what they know best – project outcomes. They won't have be burdened with administration.</p>

  <h2 class="abs section-title" style="top:2852px;font-size:40px">YOU KNOW YOUR BUSINESS, WE KNOW PMOS</h2>
  <div class="abs" style="top:2912px"><div class="rule" style="width:960px;background:var(--accent-soft)"></div></div>

  <div class="abs quick">
    <div class="rule"></div>
    <div class="quick-head">
      <svg width="64" height="64" viewBox="0 0 64 64" aria-hidden="true">
        <circle cx="32" cy="32" r="32" fill="#3a3d40"/>
        <rect x="17" y="22" width="30" height="20" fill="none" stroke="#fff" stroke-width="3"/>
        <path d="M17 22 L32 34 L47 22" fill="none" stroke="#fff" stroke-width="3"/>
      </svg>
      <span>Quick Contact</span>
    </div>
  </div>
  <form class="form">
    <div class="row"><label>Name</label><div class="field"></div></div>
    <div class="row"><label>Email</label><div class="field"></div></div>
    <div class="row"><label>Message</label><div class="field area"></div></div>
  </form>
</main>

<footer>
  <div class="abs footer" role="img" aria-label="Dark photograph of city office buildings"></div>
  <div class="abs brand footer-brand"><span class="mark"></span><span class="name">KEYSTONE PMO</span></div>
  <div class="abs social"><span></span><span></span></div>
  <nav class="abs main-nav foot-nav">
    <span>HOME</span><span>WHAT IS A PMO</span><span>HOW DOES A PMO ADD VALUE</span><span>WHAT'S THE ADVANTAGE</span><span>WHY KEYSTONE PMO</span><span>CONTACT US</span><span>BLOG</span>
  </nav>
  <p class="abs copyright">Copyright © All Rights Reserved</p>
</footer>

</body>
</html>
```